Expanding Training Company needs a powerpoint template to deliver a consistent professional image

We want to start with a ppt template that is clean and flexible.
We are a small training organisation focusing on personal effectiveness, leadership, management and change. The MD is a New Zealander living in the United Kingdom and loves the idea of the clean green image that NZ has and wants the PowerPoint template to reflect that. We are pragmatic in what we do - everything comes back to performance improvement. Our clients are big players and our presentations need to be as clean, and as professional as theirs. We need a template that is versatile and can have their logos added as necessary.
Our training tends to be very current and as such we would like to use a lot of images and less words/bullets. We have company colours, logos and fonts that we are happy with and will continue to use.

Here are our company values to give you a sense of what we are about…

As a learning organisation we are always looking to continually improve and renew, our material, ideas, and methods, and are continually on the look out for new techniques, interventions and applications that provide measurable results to our clients.

We think life is about people and relationships, and we are prepared to walk away if people don't keep their word, are untrustworthy or lack integrity, as life is just too short to work with arses.
And because we are not arses we admit when we are wrong and make good on our commitments.

For our clients its all about performance and training is a performance enhancer, we aim to provide training excellence tin all its guises that delivers performance and happy clients.

We harness the value of the team, we believe in Interdependence.

We make life easier for our clients and each other.

Flexibility, innovation and future focus/vision are what our clients can count on us for.

Work is one of many of life's great facilitators, we recognise and value the others - its not just about work.

Industry/Entity Type

It Company

Font styles to use
Other font styles liked:
• Avenir Next

Colors
abd037
9bcb3c

Requirements
Must have
• A clean look with multiple options for inserting images, tables, videos, text boxes etc
• copyright information
Nice to have
• Slide masters

```html
<!DOCTYPE html>
<html lang="en">
<head>
<meta charset="utf-8">
<title>Slide Design Idea – Part 01d</title>
<link href="https://fonts.googleapis.com/css2?family=Arimo:wght@400;700&family=Open+Sans:wght@400;600;700&display=swap" rel="stylesheet">
<style>
  :root{
    --backdrop:#3f1416;
    --heading:#6a3c3c;
    --sheet:#ffffff;
    --green:#23a455;
    --green-deep:#1c8a46;
    --lime:#8cc63f;
    --orange:#f26522;
    --slate:#4d5259;
    --pink:#f06eaa;
    --line:#c9c9c9;
    --label:#222222;
  }
  *{margin:0;padding:0;box-sizing:border-box}
  html,body{width:1200px;height:930px;overflow:hidden}
  body{background:var(--backdrop);position:relative;font-family:"Open Sans",sans-serif}
  .board-title{position:absolute;top:18px;left:0;width:1200px;text-align:center;font-family:"Arimo",sans-serif;font-weight:700;font-size:35px;color:var(--heading);letter-spacing:.3px}
  .board-sheet{position:absolute;left:13px;top:116px;width:1180px;height:728px;background:var(--sheet);
    padding:123px 0 0 17px;display:grid;grid-template-columns:repeat(6,173px);column-gap:22.2px;grid-auto-rows:120px;align-content:start}
  .thumb{display:flex;flex-direction:column;align-items:center}
  .thumb svg{width:173px;height:97px;display:block;box-shadow:0 1px 3px rgba(0,0,0,.35);background:#fff}
  .thumb-label{margin-top:9px;font-family:"Arimo",sans-serif;font-size:8.6px;color:var(--label)}
  .t-head{font-family:"Open Sans",sans-serif;font-size:8px;fill:#7a7a7a;text-anchor:middle}
  .t-tiny{font-family:"Open Sans",sans-serif;font-size:3.6px;fill:#fff;font-weight:700}
  .t-big{font-family:"Open Sans",sans-serif;font-weight:600}
</style>
</head>
<body>
<h1 class="board-title">SIDE DESIGN IDEA ( Part - 01d)</h1>

<main class="board-sheet">

  <!-- 109 -->
  <figure class="thumb">
    <svg viewBox="0 0 216 121">
      <rect x="3" y="3" width="4" height="4" fill="var(--orange)"/>
      <circle cx="202" cy="12" r="6" fill="var(--green)"/>
      <text class="t-head" x="108" y="17">Company Customization</text>
      <rect x="20" y="28" width="88" height="30" fill="var(--green)"/>
      <rect x="108" y="28" width="88" height="30" fill="var(--lime)"/>
      <rect x="20" y="58" width="88" height="30" fill="var(--orange)"/>
      <rect x="108" y="58" width="88" height="30" fill="var(--slate)"/>
      <circle cx="108" cy="58" r="7" fill="#fff"/>
      <text class="t-tiny" x="44" y="38">Title - 01</text>
      <text class="t-tiny" x="44" y="74">Title - 01</text>
      <text class="t-tiny" x="160" y="74">Title - 01</text>
      <rect x="30" y="40" width="35" height="1.4" fill="#e6f4ea"/>
      <rect x="30" y="76" width="35" height="1.4" fill="#fde2d4"/>
      <rect x="20" y="104" width="176" height="1.4" fill="var(--line)"/>
      <rect x="40" y="108" width="136" height="1.4" fill="var(--line)"/>
    </svg>
    <figcaption class="thumb-label">Slide109.JPG</figcaption>
  </figure>

  <!-- 110 -->
  <figure class="thumb">
    <svg viewBox="0 0 216 121">
      <defs><linearGradient id="g110" x1="0" y1="0" x2="1" y2="1"><stop offset="0" stop-color="#2a9a55"/><stop offset="1" stop-color="#157a3c"/></linearGradient></defs>
      <rect width="216" height="121" fill="url(#g110)" role="img" aria-label="Photo of green hills under a green colour wash"/>
      <circle cx="145" cy="75" r="26" fill="var(--orange)"/>
      <rect x="172" y="52" width="24" height="18" fill="var(--orange)"/>
      <rect x="180" y="57" width="9" height="6" fill="none" stroke="#fff" stroke-width="1"/>
      <text class="t-tiny" x="132" y="66">WELL DISPLAY</text>
      <rect x="132" y="71" width="26" height="1.3" fill="#fde2d4"/>
      <rect x="132" y="75" width="22" height="1.3" fill="#fde2d4"/>
      <rect x="132" y="79" width="24" height="1.3" fill="#fde2d4"/>
    </svg>
    <figcaption class="thumb-label">Slide110.JPG</figcaption>
  </figure>

  <!-- 111 -->
  <figure class="thumb">
    <svg viewBox="0 0 216 121">
      <text class="t-head" x="108" y="17">Our Service</text>
      <g fill="none" stroke="var(--orange)" stroke-width="1">
        <rect x="12" y="28" width="45" height="38"/><rect x="108" y="28" width="45" height="38"/><rect x="156" y="28" width="45" height="38"/>
        <rect x="12" y="70" width="45" height="38"/><rect x="60" y="70" width="45" height="38"/><rect x="108" y="70" width="45" height="38"/>
      </g>
      <rect x="60" y="28" width="45" height="38" fill="var(--orange)"/>
      <rect x="156" y="70" width="45" height="38" fill="var(--orange)"/>
      <g fill="var(--orange)">
        <rect x="30" y="34" width="9" height="6"/><rect x="126" y="34" width="8" height="7"/><rect x="174" y="34" width="8" height="7"/>
        <circle cx="34" cy="79" r="4"/><circle cx="82" cy="79" r="4"/><circle cx="130" cy="79" r="4"/>
      </g>
      <rect x="79" y="34" width="8" height="7" fill="#fff"/><rect x="175" y="76" width="8" height="7" fill="#fff"/>
      <g fill="var(--line)">
        <rect x="20" y="50" width="29" height="1.3"/><rect x="22" y="55" width="25" height="1.3"/>
        <rect x="116" y="50" width="29" height="1.3"/><rect x="164" y="50" width="29" height="1.3"/>
        <rect x="20" y="92" width="29" height="1.3"/><rect x="68" y="92" width="29" height="1.3"/><rect x="116" y="92" width="29" height="1.3"/>
      </g>
      <rect x="68" y="50" width="29" height="1.3" fill="#fff"/><rect x="164" y="92" width="29" height="1.3" fill="#fff"/>
    </svg>
    <figcaption class="thumb-label">Slide111.JPG</figcaption>
  </figure>

  <!-- 112 -->
  <figure class="thumb">
    <svg viewBox="0 0 216 121">
      <rect x="3" y="3" width="4" height="4" fill="var(--orange)"/>
      <circle cx="202" cy="12" r="6" fill="var(--green)"/>
      <text class="t-head" x="108" y="17">Product Trending</text>
      <g fill="var(--line)">
        <rect x="18" y="32" width="42" height="1.3"/><rect x="22" y="37" width="38" height="1.3"/>
        <rect x="18" y="56" width="42" height="1.3"/><rect x="22" y="61" width="38" height="1.3"/>
        <rect x="18" y="80" width="42" height="1.3"/><rect x="22" y="85" width="38" height="1.3"/>
      </g>
      <g fill="var(--green)"><rect x="66" y="29" width="11" height="15"/><rect x="79" y="29" width="11" height="15"/><rect x="92" y="29" width="11" height="15"/><rect x="105" y="29" width="11" height="15"/><rect x="118" y="29" width="11" height="15"/><rect x="131" y="29" width="11" height="15"/><rect x="144" y="29" width="11" height="15"/><rect x="157" y="29" width="11" height="15"/></g>
      <g fill="var(--orange)"><rect x="66" y="53" width="11" height="15"/><rect x="79" y="53" width="11" height="15"/><rect x="92" y="53" width="11" height="15"/><rect x="105" y="53" width="11" height="15"/><rect x="118" y="53" width="11" height="15"/><rect x="131" y="53" width="11" height="15"/><rect x="144" y="53" width="11" height="15"/><rect x="157" y="53" width="11" height="15"/></g>
      <g fill="var(--slate)"><rect x="66" y="77" width="11" height="15"/><rect x="79" y="77" width="11" height="15"/><rect x="92" y="77" width="11" height="15"/></g>
      <g fill="#d4d4d4"><rect x="170" y="29" width="11" height="15"/><rect x="183" y="29" width="11" height="15"/><rect x="170" y="53" width="11" height="15"/><rect x="183" y="53" width="11" height="15"/>
        <rect x="105" y="77" width="11" height="15"/><rect x="118" y="77" width="11" height="15"/><rect x="131" y="77" width="11" height="15"/><rect x="144" y="77" width="11" height="15"/><rect x="157" y="77" width="11" height="15"/><rect x="170" y="77" width="11" height="15"/><rect x="183" y="77" width="11" height="15"/></g>
    </svg>
    <figcaption class="thumb-label">Slide112.JPG</figcaption>
  </figure>

  <!-- 113 -->
  <figure class="thumb">
    <svg viewBox="0 0 216 121">
      <rect width="216" height="121" fill="#2ba55a"/>
      <rect y="72" width="216" height="20" fill="#3f5a4b"/>
      <text class="t-big" x="10" y="87" font-size="12" fill="#fff">MANAGEMENT</text>
      <rect x="125" y="75" width="0.8" height="14" fill="#fff"/>
      <rect x="130" y="78" width="30" height="1.4" fill="#fff"/>
      <rect x="130" y="82" width="70" height="1.1" fill="#cfd8d2"/>
      <rect x="130" y="85" width="60" height="1.1" fill="#cfd8d2"/>
    </svg>
    <figcaption class="thumb-label">Slide113.JPG</figcaption>
  </figure>

  <!-- 114 -->
  <figure class="thumb">
    <svg viewBox="0 0 216 121">
      <rect x="3" y="3" width="4" height="4" fill="var(--orange)"/>
      <circle cx="202" cy="12" r="6" fill="var(--green)"/>
      <text class="t-head" x="108" y="17">Timeline</text>
      <rect x="18" y="67" width="186" height="1" fill="#c4c4c4"/>
      <rect x="25" y="32" width="40" height="22" fill="var(--slate)"/>
      <rect x="90" y="32" width="40" height="22" fill="var(--orange)"/>
      <rect x="162" y="32" width="42" height="22" fill="var(--green)"/>
      <rect x="47" y="90" width="40" height="20" fill="var(--pink)"/>
      <rect x="128" y="90" width="42" height="20" fill="var(--lime)"/>
      <circle cx="22" cy="68" r="4" fill="var(--slate)"/><circle cx="56" cy="68" r="4" fill="var(--pink)"/>
      <circle cx="92" cy="68" r="4" fill="var(--orange)"/><circle cx="128" cy="68" r="4" fill="var(--lime)"/><circle cx="162" cy="68" r="4" fill="var(--green)"/>
      <text class="t-tiny" x="38" y="38">Title - 01</text><text class="t-tiny" x="103" y="38">Title - 01</text><text class="t-tiny" x="176" y="38">Title - 01</text>
      <text class="t-tiny" x="60" y="96">Title - 01</text><text class="t-tiny" x="142" y="96">Title - 01</text>
    </svg>
    <figcaption class="thumb-label">Slide114.JPG</figcaption>
  </figure>

  <!-- 115 -->
  <figure class="thumb">
    <svg viewBox="0 0 216 121">
      <rect x="3" y="3" width="4" height="4" fill="var(--orange)"/>
      <circle cx="202" cy="12" r="6" fill="var(--green)"/>
      <text class="t-head" x="108" y="17">Marketing Strategy</text>
      <g fill="none" stroke-width="2"><circle cx="15" cy="45" r="5" stroke="var(--green)"/><circle cx="15" cy="70" r="5" stroke="var(--green)"/><circle cx="15" cy="95" r="5" stroke="var(--green)"/></g>
      <g fill="var(--line)"><rect x="25" y="42" width="28" height="1.2"/><rect x="25" y="46" width="24" height="1.2"/><rect x="25" y="67" width="28" height="1.2"/><rect x="25" y="71" width="24" height="1.2"/><rect x="25" y="92" width="28" height="1.2"/><rect x="25" y="96" width="24" height="1.2"/></g>
      <g fill="none" stroke-width="10">
        <circle cx="110" cy="68" r="22" stroke="var(--green)" stroke-dasharray="35 103"/>
        <circle cx="110" cy="68" r="22" stroke="var(--orange)" stroke-dasharray="35 103" stroke-dashoffset="-35"/>
        <circle cx="110" cy="68" r="22" stroke="var(--slate)" stroke-dasharray="34 104" stroke-dashoffset="-70"/>
        <circle cx="110" cy="68" r="22" stroke="var(--pink)" stroke-dasharray="34 104" stroke-dashoffset="-104"/>
      </g>
      <text x="110" y="67" font-size="4.5" text-anchor="middle" fill="var(--slate)" class="t-big">MORE</text>
      <text x="110" y="72" font-size="4.5" text-anchor="middle" fill="var(--slate)" class="t-big">SALES</text>
      <text class="t-big" x="163" y="40" font-size="13" fill="var(--green)">35%</text>
      <text class="t-big" x="163" y="81" font-size="13" fill="var(--green)">15%</text>
      <g fill="var(--line)"><rect x="163" y="46" width="36" height="1.2"/><rect x="163" y="50" width="30" height="1.2"/><rect x="163" y="87" width="36" height="1.2"/><rect x="163" y="91" width="30" height="1.2"/></g>
    </svg>
    <figcaption class="thumb-label">Slide115.JPG</figcaption>
  </figure>

  <!-- 116 -->
  <figure class="thumb">
    <svg viewBox="0 0 216 121">
      <rect x="3" y="3" width="4" height="4" fill="var(--orange)"/>
      <circle cx="202" cy="12" r="6" fill="var(--green)"/>
      <text class="t-head" x="108" y="17">Company Performance</text>
      <rect x="12" y="34" width="62" height="68" fill="#e6e6e6" role="img" aria-label="Illustration of a crowd led by one person"/>
      <g fill="var(--line)"><rect x="95" y="58" width="38" height="1.3"/><rect x="95" y="62" width="32" height="1.3"/><rect x="95" y="88" width="38" height="1.3"/><rect x="95" y="92" width="32" height="1.3"/></g>
      <rect x="152" y="30" width="50" height="22" fill="var(--slate)"/>
      <rect x="152" y="57" width="50" height="22" fill="var(--orange)"/>
      <rect x="152" y="84" width="50" height="22" fill="var(--green)"/>
      <text class="t-tiny" x="156" y="36">Title - 01</text><text class="t-tiny" x="156" y="63">Title - 01</text><text class="t-tiny" x="156" y="90">Title - 01</text>
    </svg>
    <figcaption class="thumb-label">Slide116.JPG</figcaption>
  </figure>

  <!-- 117 -->
  <figure class="thumb">
    <svg viewBox="0 0 216 121">
      <rect x="3" y="3" width="4" height="4" fill="var(--orange)"/>
      <circle cx="202" cy="12" r="6" fill="var(--green)"/>
      <text class="t-head" x="108" y="17">Chart Design Idea</text>
      <path d="M15 80 L15 58 L42 42 L70 58 L95 52 L118 66 L143 46 L143 80 Z" fill="var(--slate)"/>
      <rect x="15" y="85" width="128" height="1" fill="#ddd"/>
      <rect x="158" y="30" width="46" height="40" fill="none" stroke="#bbb" stroke-width=".8"/>
      <rect x="158" y="74" width="46" height="36" fill="var(--orange)"/>
      <g fill="var(--line)"><rect x="162" y="38" width="38" height="1.2"/><rect x="162" y="42" width="32" height="1.2"/></g>
    </svg>
    <figcaption class="thumb-label">Slide117.JPG</figcaption>
  </figure>

  <!-- 118 -->
  <figure class="thumb">
    <svg viewBox="0 0 216 121">
      <rect x="3" y="3" width="4" height="4" fill="var(--orange)"/>
      <circle cx="202" cy="12" r="6" fill="var(--green)"/>
      <rect x="10" y="29" width="18" height="18" fill="var(--slate)"/>
      <rect x="10" y="69" width="18" height="18" fill="var(--slate)"/>
      <g fill="var(--line)"><rect x="32" y="32" width="20" height="1.3"/><rect x="32" y="40" width="20" height="1.3"/><rect x="10" y="55" width="50" height="1.2"/><rect x="32" y="72" width="20" height="1.3"/><rect x="32" y="80" width="20" height="1.3"/><rect x="10" y="95" width="50" height="1.2"/></g>
      <rect x="80" y="28" width="64" height="80" fill="#dff0e4" role="img" aria-label="Light bulb made of green dots"/>
      <circle cx="112" cy="58" r="24" fill="var(--lime)" opacity=".55"/>
      <rect x="105" y="86" width="14" height="12" fill="var(--lime)"/>
      <g fill="var(--line)"><rect x="160" y="32" width="40" height="1.3"/><rect x="160" y="36" width="34" height="1.3"/><rect x="160" y="52" width="40" height="1.3"/><rect x="160" y="56" width="34" height="1.3"/><rect x="160" y="72" width="40" height="1.3"/><rect x="160" y="76" width="34" height="1.3"/><rect x="160" y="92" width="40" height="1.3"/><rect x="160" y="96" width="34" height="1.3"/></g>
    </svg>
    <figcaption class="thumb-label">Slide118.JPG</figcaption>
  </figure>

  <!-- 119 -->
  <figure class="thumb">
    <svg viewBox="0 0 216 121">
      <rect width="216" height="121" fill="#2ba55a"/>
      <rect width="80" height="121" fill="#3f5a4b"/>
      <g fill="var(--green)"><circle cx="20" cy="22" r="5"/><circle cx="20" cy="47" r="5"/><circle cx="20" cy="74" r="5"/><circle cx="20" cy="101" r="5"/></g>
      <g fill="#cfd8d2"><rect x="31" y="17" width="18" height="1.4"/><rect x="31" y="21" width="40" height="1.1"/><rect x="31" y="24" width="34" height="1.1"/>
        <rect x="31" y="42" width="18" height="1.4"/><rect x="31" y="46" width="40" height="1.1"/><rect x="31" y="49" width="34" height="1.1"/>
        <rect x="31" y="69" width="18" height="1.4"/><rect x="31" y="73" width="40" height="1.1"/><rect x="31" y="76" width="34" height="1.1"/>
        <rect x="31" y="96" width="18" height="1.4"/><rect x="31" y="100" width="40" height="1.1"/><rect x="31" y="103" width="34" height="1.1"/></g>
    </svg>
    <figcaption class="thumb-label">Slide119.JPG</figcaption>
  </figure>

  <!-- 120 -->
  <figure class="thumb">
    <svg viewBox="0 0 216 121">
      <rect x="3" y="3" width="4" height="4" fill="var(--orange)"/>
      <circle cx="202" cy="12" r="6" fill="var(--green)"/>
      <text class="t-head" x="108" y="17">Slide Design Idea</text>
      <polygon points="108,36 136,50 108,64 80,50" fill="var(--slate)"/>
      <polygon points="80,50 108,64 108,100 80,86" fill="var(--green)"/>
      <polygon points="108,64 136,50 136,86 108,100" fill="var(--orange)"/>
      <polygon points="80,50 108,64 94,93 80,86" fill="var(--lime)"/>
      <rect x="12" y="30" width="44" height="20" fill="var(--slate)"/><rect x="160" y="30" width="44" height="20" fill="var(--slate)"/>
      <rect x="6" y="58" width="40" height="20" fill="var(--green)"/><rect x="170" y="58" width="40" height="20" fill="var(--green)"/>
      <rect x="12" y="88" width="44" height="20" fill="var(--lime)"/><rect x="160" y="88" width="44" height="20" fill="var(--orange)"/>
    </svg>
    <figcaption class="thumb-label">Slide120.JPG</figcaption>
  </figure>

  <!-- 121 -->
  <figure class="thumb">
    <svg viewBox="0 0 216 121">
      <rect width="216" height="121" fill="#2ba55a"/>
      <circle cx="48" cy="62" r="24" fill="var(--orange)"/>
      <circle cx="108" cy="62" r="24" fill="var(--slate)"/>
      <circle cx="168" cy="62" r="24" fill="var(--green-deep)"/>
      <text class="t-tiny" x="41" y="64">Title - 01</text><text class="t-tiny" x="101" y="64">Title - 01</text><text class="t-tiny" x="161" y="64">Title - 01</text>
      <g fill="#fff"><rect x="44" y="46" width="8" height="8"/><circle cx="108" cy="50" r="4"/><circle cx="168" cy="50" r="4"/></g>
    </svg>
    <figcaption class="thumb-label">Slide121.JPG</figcaption>
  </figure>

  <!-- 122 -->
  <figure class="thumb">
    <svg viewBox="0 0 216 121">
      <rect x="3" y="3" width="4" height="4" fill="var(--orange)"/>
      <circle cx="202" cy="12" r="6" fill="var(--green)"/>
      <text class="t-head" x="108" y="17">Key performance</text>
      <rect x="22" y="33" width="12" height="8" fill="none" stroke="var(--green)" stroke-width="1.5"/>
      <path d="M62 32 l10 10 M72 32 l-10 10" stroke="var(--orange)" stroke-width="2"/>
      <circle cx="108" cy="37" r="5" fill="none" stroke="var(--lime)" stroke-width="1.5"/>
      <circle cx="146" cy="37" r="5" fill="none" stroke="var(--slate)" stroke-width="1.5"/>
      <rect x="180" y="32" width="9" height="11" fill="none" stroke="var(--orange)" stroke-width="1.5"/>
      <rect x="10" y="64" width="36" height="24" fill="var(--green)"/>
      <rect x="49" y="64" width="36" height="24" fill="var(--orange)"/>
      <rect x="89" y="64" width="36" height="24" fill="var(--lime)"/>
      <rect x="128" y="64" width="36" height="24" fill="var(--slate)"/>
      <rect x="167" y="64" width="36" height="24" fill="var(--orange)"/>
      <rect x="10" y="61" width="193" height="1" fill="#999"/>
      <g fill="var(--line)"><rect x="40" y="100" width="60" height="1.2"/><rect x="120" y="100" width="60" height="1.2"/></g>
    </svg>
    <figcaption class="thumb-label">Slide122.JPG</figcaption>
  </figure>

  <!-- 123 -->
  <figure class="thumb">
    <svg viewBox="0 0 216 121">
      <rect x="3" y="3" width="4" height="4" fill="var(--orange)"/>
      <circle cx="202" cy="12" r="6" fill="var(--green)"/>
      <text class="t-head" x="108" y="17">Maintenance Cost</text>
      <g fill="none" stroke-width="2.5" stroke-dasharray="1.5 1.5">
        <circle cx="34" cy="48" r="15" stroke="var(--lime)"/>
        <circle cx="82" cy="48" r="15" stroke="var(--green)"/>
        <circle cx="134" cy="48" r="15" stroke="var(--green)"/>
        <circle cx="182" cy="48" r="15" stroke="var(--slate)"/>
      </g>
      <circle cx="134" cy="48" r="10" fill="var(--green)"/>
      <circle cx="182" cy="48" r="10" fill="var(--slate)"/>
      <text x="34" y="51" font-size="7" text-anchor="middle" fill="#e7d84a" class="t-big">35%</text>
      <text x="82" y="51" font-size="7" text-anchor="middle" fill="var(--orange)" class="t-big">75%</text>
      <text x="134" y="51" font-size="6" text-anchor="middle" fill="#fff" class="t-big">30%</text>
      <text x="182" y="51" font-size="6" text-anchor="middle" fill="#fff" class="t-big">60%</text>
      <rect x="118" y="73" width="34" height="22" fill="var(--green)"/>
      <rect x="166" y="73" width="34" height="22" fill="var(--slate)"/>
      <g fill="var(--line)"><rect x="18" y="80" width="34" height="1.2"/><rect x="20" y="84" width="30" height="1.2"/><rect x="66" y="80" width="34" height="1.2"/><rect x="68" y="84" width="30" height="1.2"/></g>
    </svg>
    <figcaption class="thumb-label">Slide123.JPG</figcaption>
  </figure>

  <!-- 124 -->
  <figure class="thumb">
    <svg viewBox="0 0 216 121">
      <rect x="3" y="3" width="4" height="4" fill="var(--orange)"/>
      <circle cx="202" cy="12" r="6" fill="var(--green)"/>
      <text class="t-head" x="108" y="17">Market Share</text>
      <ellipse cx="108" cy="70" rx="37" ry="14" fill="#166b35"/>
      <ellipse cx="108" cy="64" rx="37" ry="14" fill="var(--green)"/>
      <path d="M108 64 L108 50 A37 14 0 0 1 143 60 Z" fill="var(--orange)"/>
      <path d="M108 64 L143 60 A37 14 0 0 1 128 76 Z" fill="var(--slate)"/>
      <text x="52" y="42" font-size="7" fill="var(--slate)">20%</text>
      <text x="52" y="88" font-size="7" fill="var(--slate)">40%</text>
      <text x="142" y="42" font-size="7" fill="var(--slate)">10%</text>
      <text x="142" y="88" font-size="7" fill="var(--slate)">30%</text>
      <rect x="10" y="28" width="38" height="24" fill="var(--lime)"/>
      <rect x="10" y="72" width="38" height="24" fill="var(--green)"/>
      <rect x="162" y="28" width="38" height="24" fill="var(--orange)"/>
      <rect x="162" y="72" width="38" height="24" fill="var(--slate)"/>
    </svg>
    <figcaption class="thumb-label">Slide124.JPG</figcaption>
  </figure>

  <!-- 125 -->
  <figure class="thumb">
    <svg viewBox="0 0 216 121">
      <rect x="3" y="3" width="4" height="4" fill="var(--orange)"/>
      <circle cx="202" cy="12" r="6" fill="var(--green)"/>
      <text class="t-head" x="108" y="17">Slide Design Idea</text>
      <rect x="56" y="32" width="14" height="9" fill="none" stroke="var(--orange)" stroke-width="1.5"/>
      <polygon points="63,50 70,62 56,62" fill="var(--green)"/>
      <polygon points="56,62 70,62 77,74 49,74" fill="var(--orange)"/>
      <polygon points="49,74 77,74 84,86 42,86" fill="var(--slate)"/>
      <polygon points="42,86 84,86 92,100 34,100" fill="var(--lime)"/>
      <g fill="none" stroke-width="1.3"><circle cx="155" cy="38" r="5" stroke="var(--green)"/><circle cx="155" cy="60" r="5" stroke="var(--orange)"/><circle cx="155" cy="82" r="5" stroke="var(--slate)"/></g>
      <g fill="var(--line)"><rect x="166" y="35" width="34" height="1.2"/><rect x="166" y="39" width="28" height="1.2"/><rect x="166" y="57" width="34" height="1.2"/><rect x="166" y="61" width="28" height="1.2"/><rect x="166" y="79" width="34" height="1.2"/><rect x="166" y="83" width="28" height="1.2"/><rect x="166" y="101" width="34" height="1.2"/></g>
    </svg>
    <figcaption class="thumb-label">Slide125.JPG</figcaption>
  </figure>

  <!-- 126 -->
  <figure class="thumb">
    <svg viewBox="0 0 216 121">
      <rect width="216" height="121" fill="#2ba55a"/>
      <text x="108" y="38" font-size="12" text-anchor="middle" fill="#fff" class="t-big">Company</text>
      <rect x="40" y="43" width="136" height="1.2" fill="#d9efe0"/>
      <rect x="50" y="47" width="116" height="1.2" fill="#d9efe0"/>
      <rect x="30" y="57" width="0" height="0"/>
      <rect x="28" y="58" width="50" height="24" fill="var(--orange)"/>
      <rect x="83" y="58" width="50" height="24" fill="var(--slate)"/>
      <rect x="138" y="58" width="50" height="24" fill="var(--green-deep)"/>
      <text class="t-tiny" x="46" y="64">Title - 01</text><text class="t-tiny" x="101" y="64">Title - 01</text><text class="t-tiny" x="156" y="64">Title - 01</text>
    </svg>
    <figcaption class="thumb-label">Slide126.JPG</figcaption>
  </figure>

  <!-- 127 -->
  <figure class="thumb">
    <svg viewBox="0 0 216 121">
      <circle cx="202" cy="12" r="6" fill="var(--green)"/>
      <g fill="#3a3a3a">
        <rect x="22" y="10" width="8" height="7"/><rect x="42" y="10" width="7" height="7"/><rect x="62" y="10" width="8" height="7"/><rect x="82" y="10" width="7" height="7"/><rect x="102" y="10" width="8" height="7"/><rect x="122" y="10" width="7" height="7"/><rect x="142" y="10" width="8" height="7"/><rect x="162" y="10" width="7" height="7"/><rect x="182" y="10" width="7" height="7"/>
        <circle cx="26" cy="32" r="4"/><circle cx="46" cy="32" r="4"/><circle cx="66" cy="32" r="4"/><circle cx="86" cy="32" r="4"/><circle cx="106" cy="32" r="4"/><circle cx="126" cy="32" r="4"/><circle cx="146" cy="32" r="4"/><circle cx="166" cy="32" r="4"/><circle cx="186" cy="32" r="4"/><circle cx="206" cy="32" r="4"/>
        <rect x="22" y="44" width="8" height="7"/><rect x="42" y="44" width="7" height="7"/><rect x="62" y="44" width="8" height="7"/><rect x="82" y="44" width="7" height="7"/><rect x="102" y="44" width="8" height="7"/><rect x="122" y="44" width="7" height="7"/><rect x="142" y="44" width="8" height="7"/><rect x="162" y="44" width="7" height="7"/><rect x="182" y="44" width="7" height="7"/><rect x="202" y="44" width="7" height="7"/>
        <circle cx="26" cy="65" r="4"/><circle cx="46" cy="65" r="4"/><circle cx="66" cy="65" r="4"/><circle cx="86" cy="65" r="4"/><circle cx="106" cy="65" r="4"/><circle cx="126" cy="65" r="4"/><circle cx="146" cy="65" r="4"/><circle cx="166" cy="65" r="4"/><circle cx="186" cy="65" r="4"/><circle cx="206" cy="65" r="4"/>
        <rect x="22" y="77" width="8" height="7"/><rect x="42" y="77" width="7" height="7"/><rect x="62" y="77" width="8" height="7"/><rect x="82" y="77" width="7" height="7"/><rect x="102" y="77" width="8" height="7"/><rect x="122" y="77" width="7" height="7"/><rect x="142" y="77" width="8" height="7"/><rect x="162" y="77" width="7" height="7"/><rect x="182" y="77" width="7" height="7"/><rect x="202" y="77" width="7" height="7"/>
        <circle cx="26" cy="98" r="4"/><circle cx="46" cy="98" r="4"/><circle cx="66" cy="98" r="4"/><circle cx="86" cy="98" r="4"/><circle cx="106" cy="98" r="4"/><circle cx="126" cy="98" r="4"/><circle cx="146" cy="98" r="4"/><circle cx="166" cy="98" r="4"/><circle cx="186" cy="98" r="4"/><circle cx="206" cy="98" r="4"/>
        <rect x="22" y="108" width="8" height="7"/><rect x="42" y="108" width="7" height="7"/><rect x="62" y="108" width="8" height="7"/><rect x="82" y="108" width="7" height="7"/><rect x="102" y="108" width="8" height="7"/><rect x="122" y="108" width="7" height="7"/><rect x="142" y="108" width="8" height="7"/><rect x="162" y="108" width="7" height="7"/><rect x="182" y="108" width="7" height="7"/>
      </g>
    </svg>
    <figcaption class="thumb-label">Slide127.JPG</figcaption>
  </figure>

  <!-- 128 -->
  <figure class="thumb">
    <svg viewBox="0 0 216 121">
      <defs><linearGradient id="g128" x1="0" y1="0" x2="1" y2="1"><stop offset="0" stop-color="#2a9a55"/><stop offset="1" stop-color="#17773b"/></linearGradient></defs>
      <rect width="216" height="121" fill="url(#g128)" role="img" aria-label="Aerial photo of a city under a green colour wash"/>
      <path d="M186 28 a5 5 0 0 1 10 0 c0 5 -5 10 -5 10 c0 0 -5 -5 -5 -10 Z" fill="var(--orange)"/>
      <rect y="75" width="216" height="20" fill="#2ba55a"/>
      <rect x="0" y="75" width="42" height="20" fill="var(--slate)"/>
      <rect x="86" y="75" width="42" height="20" fill="var(--lime)"/>
      <rect x="128" y="75" width="42" height="20" fill="var(--slate)"/>
      <g fill="#e9f2ec"><rect x="6" y="86" width="30" height="1.1"/><rect x="6" y="89" width="26" height="1.1"/><rect x="48" y="85" width="30" height="1.1"/><rect x="94" y="88" width="26" height="1.1"/><rect x="136" y="88" width="26" height="1.1"/><rect x="178" y="85" width="28" height="1.1"/></g>
      <rect x="19" y="79" width="4" height="5" fill="#fff"/><rect x="105" y="79" width="4" height="5" fill="#fff"/><circle cx="149" cy="81" r="2.5" fill="#fff"/>
    </svg>
    <figcaption class="thumb-label">Slide128.JPG</figcaption>
  </figure>

  <!-- 129 -->
  <figure class="thumb">
    <svg viewBox="0 0 216 121">
      <rect width="216" height="121" fill="var(--green)"/>
      <text x="108" y="60" font-size="13" text-anchor="middle" fill="#fff" class="t-big">THANKS</text>
      <rect x="98" y="64" width="20" height="1" fill="var(--orange)"/>
      <rect x="20" y="70" width="176" height="1.1" fill="#cdebd7"/>
      <rect x="30" y="74" width="156" height="1.1" fill="#cdebd7"/>
    </svg>
    <figcaption class="thumb-label">Slide129.JPG</figcaption>
  </figure>

</main>
</body>
</html>
```